Q7 Engineering Rail Sector Brochure

We need a new 3 page folding brochure for Q7 Engineering Pty Ltd. The organisation is currently supporting customers in Defence, Maritime and Information and Communications Technology companies. We are currently looking to expand our engineering services into the rail sector by providing manpower and consultancy services to railway sector clients.We would like the brochure to be based on an A4 page and look technical with particular focus on communications systems used within the railways. This could include pictures of rail control centres, trains (Australian trains only please), train radio communications equipment, radio antennas, computers and networking equipment. Please use both graphics and photos.The brochure will be provided to potential rail customers and should be clear and uncluttered.The following is our company website: www.q7engineering.com.au if you would like more detail on our current work.I have attached the file for our logo which should appear on the brochure.
Target Market(s)
Providing manpower and consultancy services to the railway sector. This includes rail companies (e.g. Harwick Loop Trains, T/Run etc) and rail equipment and carriage suppliers (e.g. Falverine)
Colors
Designer to choose colors to be used in the design.
Requirements
Must have
- Instead of having "lorem ipsum" text in the brochure you can please use some of the text in the file we have provided. Not all has to be used, and you should not be limited to what is in the file.
Nice to have
- Mixture of different font sizes to highlight particular text elements.

```html
<!DOCTYPE html>
<html lang="en">
<head>
<meta charset="utf-8">
<title>Q7 Engineering Rail Sector Brochure</title>
<link href="https://fonts.googleapis.com/css2?family=Michroma&family=Montserrat:wght@500;600;700;800&family=Open+Sans:wght@400;600&display=swap" rel="stylesheet">
<style>
:root{
  --blue:#1a67bd;
  --blue-dark:#134f94;
  --teal:#3cc39a;
  --grey:#4a4d52;
  --grey-mid:#8e959d;
  --paper:#f2f3f4;
  --paper-edge:#e4e6e8;
  --text:#5a5f66;
  --bg:#d9dadc;
}
*{margin:0;padding:0;box-sizing:border-box}
html,body{width:1200px;height:2571px;overflow:hidden;background:var(--bg)}
body{position:relative;font-family:"Open Sans",Arial,sans-serif;color:var(--text)}
.sheet{position:absolute;background:var(--paper);box-shadow:0 6px 22px rgba(0,0,0,.18);overflow:hidden}
.sheet--cover{left:413px;top:40px;width:373px;height:792px}
.sheet--outside{left:40px;top:892px;width:1120px;height:792px}
.sheet--inside{left:40px;top:1744px;width:1120px;height:792px}
.deco{position:absolute;left:0;top:0}
.panel{position:absolute;top:0;width:373px;height:792px}
.panel--1{left:0}.panel--2{left:373px}.panel--3{left:747px}
.fold{position:absolute;top:0;width:1px;height:792px;background:var(--paper-edge)}

/* cover */
.cover{position:absolute;inset:0}
.brand{position:absolute;display:flex;align-items:center;gap:8px;font-family:"Montserrat",sans-serif;font-weight:700}
.brand__dot{width:14px;height:14px;border-radius:50%;background:currentColor}
.cover .brand{left:0;right:0;top:40px;justify-content:center;color:#fff;font-size:24px}
.headline{position:absolute;left:0;right:0;top:520px;text-align:center}
.headline__line{font-family:"Michroma",sans-serif;line-height:1.15;letter-spacing:.5px}
.headline__line--a{color:var(--blue);font-size:21px}
.headline__line--b{color:var(--grey-mid);font-size:26px}
.headline__line--c{color:var(--blue);font-size:33px}
.headline__tag{margin-top:8px;font-family:"Montserrat",sans-serif;font-weight:700;font-size:9.5px;color:var(--grey);letter-spacing:.4px}
.cover__web{position:absolute;left:0;right:0;top:690px;text-align:center;font-family:"Montserrat",sans-serif;font-weight:800;font-size:15px;color:var(--grey)}

/* text blocks */
.block{position:absolute;left:36px;right:30px}
.heading{font-family:"Montserrat",sans-serif;font-weight:800;color:var(--blue);text-transform:uppercase;line-height:1.2}
.heading--lg{font-size:16px}
.heading--md{font-size:13px;margin:16px 0 8px}
.copy{font-size:10px;line-height:1.55;margin-top:8px}
.ticks{list-style:none;margin-top:8px}
.ticks li{position:relative;padding-left:18px;font-size:10px;line-height:1.4;margin-bottom:6px}
.ticks li::before{content:"";position:absolute;left:0;top:1px;width:11px;height:11px;border-radius:50%;background:var(--teal)}
.ticks li::after{content:"";position:absolute;left:3px;top:3.5px;width:5px;height:3px;border-left:1.5px solid #fff;border-bottom:1.5px solid #fff;transform:rotate(-45deg)}

/* contact */
.contact{position:absolute;left:0;right:0;top:290px;text-align:center}
.contact .brand{position:static;justify-content:center;color:var(--blue);font-size:21px}
.contact__title{margin-top:50px;font-family:"Montserrat",sans-serif;font-weight:800;font-size:16px;color:var(--blue)}
.contact__item{margin-top:14px;font-family:"Montserrat",sans-serif;font-weight:600;font-size:13px;color:var(--grey);line-height:1.45}
.contact__icon{display:block;margin:0 auto 4px}

/* inside */
.trust{position:absolute;left:0;right:0;top:28px;text-align:center;font-family:"Montserrat",sans-serif;font-weight:800;font-size:15px;line-height:1.3;color:#fff}
.experience{position:absolute;left:30px;right:26px;top:310px}
.exp-grid{display:grid;grid-template-columns:repeat(3,1fr);row-gap:14px;margin-top:18px}
.exp{text-align:center}
.exp__img{width:62px;height:62px;border-radius:50%;margin:0 auto;border:3px solid #fff;box-shadow:0 1px 3px rgba(0,0,0,.2)}
.exp__img--net{background:linear-gradient(135deg,#3a6f9c,#9fb7c9)}
.exp__img--cc{background:linear-gradient(135deg,#2d3a4a,#5e87ad)}
.exp__img--ship{background:linear-gradient(135deg,#8aa3b8,#4e6173)}
.exp__img--radar{background:linear-gradient(135deg,#1c3550,#4c79a4)}
.exp__img--e3{background:linear-gradient(135deg,#2f8f3f,#e0c23a)}
.exp__img--lhd{background:linear-gradient(135deg,#a9bccc,#60798e)}
.exp__img--air{background:linear-gradient(135deg,#8fb5d8,#dfe8f0)}
.exp__img--civ{background:linear-gradient(135deg,#5a6c7c,#b8c6d2)}
.exp__label{margin-top:5px;font-family:"Montserrat",sans-serif;font-weight:800;font-size:8.5px;color:var(--blue);text-transform:uppercase;line-height:1.2}
</style>
</head>
<body>

<!-- Front cover -->
<section class="sheet sheet--cover" aria-label="Front cover">
  <div class="cover">
    <svg class="deco" width="373" height="792" viewBox="0 0 373 792">
      <defs>
        <linearGradient id="trainA" x1="0" y1="0" x2="1" y2="1">
          <stop offset="0" stop-color="#7f9bb0"/><stop offset=".55" stop-color="#4e6576"/><stop offset="1" stop-color="#c9a93a"/>
        </linearGradient>
      </defs>
      <path d="M0 0H373V230Q300 330 186 330Q70 330 0 400Z" fill="var(--blue)"/>
      <polygon points="340,350 390,350 390,420 460,420 460,470 390,470 390,560 340,560 340,470 270,470 270,420 340,420" fill="var(--grey)"/>
      <path d="M0 470Q60 470 80 430L100 440Q80 500 0 500Z" fill="var(--teal)"/>
      <circle cx="186" cy="300" r="152" fill="var(--teal)"/>
      <circle cx="196" cy="296" r="126" fill="url(#trainA)" role="img" aria-label="Photo of suburban trains on rail tracks under a station canopy"/>
    </svg>
    <div class="brand"><span class="brand__dot"></span>Q7 Engineering</div>
    <div class="headline">
      <div class="headline__line headline__line--a">SMART SOLUTIONS</div>
      <div class="headline__line headline__line--b">THAT DELIVER</div>
      <div class="headline__line headline__line--c">EXCELLENCE</div>
      <div class="headline__tag">WE DELIVER SOLUTIONS TO CRITICAL CHALLENGES</div>
    </div>
    <div class="cover__web">www.q7engineering.com.au</div>
  </div>
</section>

<!-- Outside spread -->
<section class="sheet sheet--outside" aria-label="Outside spread">
  <svg class="deco" width="1120" height="792" viewBox="0 0 1120 792">
    <defs>
      <linearGradient id="tram" x1="0" y1="0" x2="1" y2="1">
        <stop offset="0" stop-color="#dfe5ea"/><stop offset=".5" stop-color="#e4c33a"/><stop offset="1" stop-color="#3d4f60"/>
      </linearGradient>
    </defs>
    <circle cx="150" cy="50" r="178" fill="var(--teal)"/>
    <circle cx="140" cy="40" r="158" fill="url(#tram)" role="img" aria-label="Photo of a yellow light rail tram in a city street"/>
    <path d="M300 20Q360 0 430 20L425 36Q360 18 305 36Z" fill="var(--teal)"/>
    <polygon points="420,40 480,40 480,120 560,120 560,180 480,180 480,270 420,270 420,180 340,180 340,120 420,120" fill="var(--grey)"/>
  </svg>
  <div class="fold" style="left:373px"></div>
  <div class="fold" style="left:747px"></div>

  <div class="panel panel--1">
    <div class="block" style="top:232px">
      <h2 class="heading heading--lg">About Us</h2>
      <p class="copy">Q7 Engineering is an Australian consulting and engineering firm specialising in Command and Control, Communications and Network systems. We provide manpower and consultancy services to defence, maritime and rail clients, and apply systematic engineering to complex problems in these areas, including:</p>
      <ul class="ticks">
        <li>Command and Control (C2) system integration</li>
        <li>Voice and secure data radio communications</li>
        <li>Shock, vibration, noise and acoustics analysis</li>
        <li>RF system integration, modelling and simulation</li>
        <li>Networked systems, CCTV and cyber technologies</li>
        <li>Logistics, training and ongoing program support services</li>
      </ul>
    </div>
  </div>

  <div class="panel panel--2">
    <div class="contact">
      <div class="brand"><span class="brand__dot"></span>Q7 Engineering</div>
      <div class="contact__title">CONTACT US</div>
      <div class="contact__item">
        <svg class="contact__icon" width="22" height="22" viewBox="0 0 22 22"><circle cx="11" cy="11" r="11" fill="var(--teal)"/><path d="M11 5a4 4 0 0 0-4 4c0 3 4 8 4 8s4-5 4-8a4 4 0 0 0-4-4zm0 5.5a1.5 1.5 0 1 1 0-3 1.5 1.5 0 0 1 0 3z" fill="#fff"/></svg>
        Level 4, 18 Carrow St<br>Brinmere 3000
      </div>
      <div class="contact__item">
        <svg class="contact__icon" width="22" height="22" viewBox="0 0 22 22"><circle cx="11" cy="11" r="11" fill="var(--teal)"/><circle cx="11" cy="11" r="5.5" fill="none" stroke="#fff" stroke-width="1.4"/><path d="M5.5 11h11M11 5.5c-2.5 3-2.5 8 0 11M11 5.5c2.5 3 2.5 8 0 11" fill="none" stroke="#fff" stroke-width="1.2"/></svg>
        www.q7engineering.com.au
      </div>
      <div class="contact__item">
        <svg class="contact__icon" width="22" height="22" viewBox="0 0 22 22"><circle cx="11" cy="11" r="11" fill="var(--teal)"/><rect x="5.5" y="7" width="11" height="8" fill="none" stroke="#fff" stroke-width="1.4"/><path d="M5.5 7l5.5 4.5L16.5 7" fill="none" stroke="#fff" stroke-width="1.4"/></svg>
        website@q7engineering.com.au
      </div>
    </div>
  </div>

  <div class="panel panel--3">
    <div class="cover">
      <svg class="deco" width="373" height="792" viewBox="0 0 373 792">
        <defs>
          <linearGradient id="trainB" x1="0" y1="0" x2="1" y2="1">
            <stop offset="0" stop-color="#7f9bb0"/><stop offset=".55" stop-color="#4e6576"/><stop offset="1" stop-color="#c9a93a"/>
          </linearGradient>
        </defs>
        <path d="M0 0H373V230Q300 330 186 330Q70 330 0 400Z" fill="var(--blue)"/>
        <polygon points="340,350 390,350 390,420 460,420 460,470 390,470 390,560 340,560 340,470 270,470 270,420 340,420" fill="var(--grey)"/>
        <path d="M0 470Q60 470 80 430L100 440Q80 500 0 500Z" fill="var(--teal)"/>
        <circle cx="186" cy="300" r="152" fill="var(--teal)"/>
        <circle cx="196" cy="296" r="126" fill="url(#trainB)" role="img" aria-label="Photo of suburban trains on rail tracks under a station canopy"/>
      </svg>
      <div class="brand"><span class="brand__dot"></span>Q7 Engineering</div>
      <div class="headline">
        <div class="headline__line headline__line--a">SMART SOLUTIONS</div>
        <div class="headline__line headline__line--b">THAT DELIVER</div>
        <div class="headline__line headline__line--c">EXCELLENCE</div>
        <div class="headline__tag">WE DELIVER SOLUTIONS TO CRITICAL CHALLENGES</div>
      </div>
      <div class="cover__web">www.q7engineering.com.au</div>
    </div>
  </div>
</section>

<!-- Inside spread -->
<section class="sheet sheet--inside" aria-label="Inside spread">
  <svg class="deco" width="1120" height="792" viewBox="0 0 1120 792">
    <defs>
      <linearGradient id="redTrain" x1="0" y1="0" x2="1" y2="1">
        <stop offset="0" stop-color="#6f9a5a"/><stop offset=".5" stop-color="#c8343a"/><stop offset="1" stop-color="#3d4a55"/>
      </linearGradient>
    </defs>
    <polygon points="40,690 100,690 100,740 170,740 170,800 100,800 100,800 40,800 40,800 -30,800 -30,740 40,740" fill="var(--grey)"/>
    <path d="M150 792Q240 700 360 730L356 748Q250 722 178 792Z" fill="var(--teal)"/>
    <path d="M380 0H740V70Q700 130 560 130Q420 130 380 70Z" fill="var(--blue)"/>
    <path d="M740 70Q720 150 640 160L636 146Q708 132 726 66Z" fill="var(--teal)"/>
    <polygon points="682,115 718,115 718,160 760,160 760,200 718,200 718,255 682,255 682,200 654,200 654,160 682,160" fill="var(--grey)"/>
    <circle cx="1010" cy="55" r="150" fill="var(--teal)"/>
    <circle cx="1020" cy="45" r="132" fill="url(#redTrain)" role="img" aria-label="Photo of a red light rail tram beside a green park"/>
  </svg>
  <div class="fold" style="left:373px"></div>
  <div class="fold" style="left:747px"></div>

  <div class="panel panel--1">
    <div class="block" style="top:50px">
      <h2 class="heading heading--lg">Q7 Engineering offers insight and ingenuity to solve critical challenges safely</h2>
      <p class="copy">Q7 Engineering staff have been in the forefront of major program deliveries to defence and commercial customers for decades. Our staff are leaders in their field and pioneers in the establishment of systematic approaches to the most complex problems.</p>
      <h3 class="heading heading--md">Network Systems – 40%</h3>
      <ul class="ticks">
        <li>Defence Classified Networking</li>
        <li>Cryptographic Systems design</li>
        <li>High Speed Data Communications</li>
        <li>IP Voice Communications Systems Integration</li>
        <li>Information and Cybersecurity solutions</li>
      </ul>
      <h3 class="heading heading--md">Communications Systems – 35%</h3>
      <ul class="ticks">
        <li>Secure communications architecture</li>
        <li>Wideband Data Links and WiFi</li>
        <li>Microwave and Satellite Communications</li>
        <li>Custom/Speciality Antennas and RF Systems</li>
        <li>Anti-Jam Communications links</li>
      </ul>
    </div>
  </div>

  <div class="panel panel--2">
    <div class="trust">A TRUSTED PROVIDER<br>TO THE WORLD'S MOST<br>EXACTING CUSTOMERS</div>
    <div class="block" style="top:180px;right:105px">
      <h3 class="heading heading--md">Command and Control Systems – 20%</h3>
      <ul class="ticks">
        <li>Human Factors design and development</li>
        <li>Command System integration</li>
        <li>UHD TV and Video Wall display design</li>
        <li>C2 Network integration</li>
      </ul>
    </div>
    <div class="block" style="top:330px">
      <h3 class="heading heading--md">Sensor Systems – 5%</h3>
      <ul class="ticks">
        <li>Thermal monitoring</li>
        <li>Data Logging and Analysis</li>
        <li>IoT Sensor integration</li>
        <li>Shock, Vibration and Acoustics inspection and test services</li>
      </ul>
      <p class="copy">At Q7 Engineering we have a broad mix of capabilities, including abilities in the areas of networking, communications and C2 system integration. Our staff have supported the delivery of major defence and commercial programs across Australia, building secure data networks, radio systems and control centres for land, sea and air platforms. We now bring this experience to rail operators that depend on reliable communications under demanding environmental conditions.</p>
    </div>
  </div>

  <div class="panel panel--3">
    <p class="copy" style="position:absolute;left:30px;right:26px;top:228px">At Q7 Engineering, we are committed to delivering value to all our customers and users in a manner that inspires confidence and lasting trust.</p>
    <div class="experience">
      <h2 class="heading heading--lg">Our Experience</h2>
      <div class="exp-grid">
        <div class="exp"><div class="exp__img exp__img--net" role="img" aria-label="Photo of networking equipment"></div><div class="exp__label">Networking</div></div>
        <div class="exp"><div class="exp__img exp__img--cc" role="img" aria-label="Photo of a command and control room"></div><div class="exp__label">Command &amp; Control</div></div>
        <div class="exp"><div class="exp__img exp__img--ship" role="img" aria-label="Photo of a naval frigate at sea"></div><div class="exp__label">Frigate Ship</div></div>
        <div class="exp"><div class="exp__img exp__img--radar" role="img" aria-label="Photo of radar equipment"></div><div class="exp__label">Radar Systems</div></div>
        <div class="exp"><div class="exp__img exp__img--e3" role="img" aria-label="Electromagnetic field analysis plot"></div><div class="exp__label">E3 Analysis</div></div>
        <div class="exp"><div class="exp__img exp__img--lhd" role="img" aria-label="Photo of a landing ship"></div><div class="exp__label">Landing Ship</div></div>
        <div class="exp"><div class="exp__img exp__img--air" role="img" aria-label="Photo of a patrol aircraft in flight"></div><div class="exp__label">Patrol Aircraft</div></div>
        <div class="exp"><div class="exp__img exp__img--civ" role="img" aria-label="Photo of a civilian airliner"></div><div class="exp__label">Civilian Aircraft</div></div>
      </div>
    </div>
  </div>
</section>

</body>
</html>
```